Corin Abbott Business Cards

We Need two Business Cards with bleeds. the only difference between the two cards is the backaround color one lilac and pink. Attached we have the cards please match up the logo's and text. Take out the orange box out.

Target Market(s)

double-sided business cards

Industry/Entity Type

Business

Logo Text

match up as best as possible

Colors
f59195
d2a4cc

Requirements
Must have
• n/a
Nice to have
• n/a
Should not have
• n/a

```html
<!DOCTYPE html>
<html lang="en">
<head>
<meta charset="utf-8">
<title>Corin Abbott-Whitmore MD – Business Cards</title>
<link rel="stylesheet" href="https://fonts.googleapis.com/css2?family=Montserrat:wght@400;500&family=Great+Vibes&display=swap">
<style>
  :root {
    --canvas: #eeeae6;
    --pink: #f59195;
    --lilac: #d2a4cc;
    --ink: #ffffff;
    --shadow: rgba(0,0,0,0.25);
  }
  * { margin: 0; padding: 0; box-sizing: border-box; }
  html, body { width: 1200px; height: 1000px; overflow: hidden; }
  body {
    position: relative;
    background: var(--canvas);
    font-family: "Montserrat", sans-serif;
    color: var(--ink);
  }
  .card {
    position: absolute;
    width: 359px;
    height: 620px;
    box-shadow: 4px 5px 10px var(--shadow);
  }
  .card--pink { left: 193px; top: 70px; background: var(--pink); }
  .card--lilac { left: 642px; top: 295px; background: var(--lilac); }
  .card > * { position: absolute; }
  .centered { left: 0; width: 100%; text-align: center; white-space: nowrap; }
  .brand-mark {
    left: 50%;
    transform: translateX(-50%);
    border-radius: 50%;
    display: flex;
    align-items: center;
    justify-content: center;
    text-align: center;
    font-weight: 500;
    font-size: 13px;
    line-height: 1.3;
  }
  .card--pink .brand-mark { top: 40px; width: 124px; height: 124px; background: var(--ink); color: var(--pink); }
  .card--lilac .brand-mark { top: 25px; width: 118px; height: 118px; border: 2px solid var(--ink); color: var(--ink); }
  .doctor-name { font-size: 21px; font-weight: 500; letter-spacing: 0.3px; }
  .credential { font-size: 13px; }
  .specialty { font-size: 14px; }
  .specialty--script { font-family: "Great Vibes", cursive; font-size: 22px; line-height: 29px; }
  .appointment { font-size: 11px; }
  .services { list-style: none; font-size: 15px; line-height: 30px; }
  .card--lilac .services { font-size: 14px; line-height: 23px; }
  .address { font-size: 13.5px; line-height: 24px; }
  .contact { display: flex; align-items: center; font-size: 13.5px; white-space: nowrap; }
  .contact svg { width: 18px; height: 16px; margin-right: 16px; fill: var(--ink); flex: none; }
</style>
</head>
<body>

<svg width="0" height="0" style="position:absolute">
  <defs>
    <symbol id="icon-phone" viewBox="0 0 18 16"><path d="M1 5c0-3 4-4 8-4s8 1 8 4l-4 1-1-2H6L5 6 1 5z"/><path d="M4 8h10l2 7H2z"/><circle cx="9" cy="11" r="2" fill="currentColor"/></symbol>
    <symbol id="icon-fax" viewBox="0 0 18 16"><rect x="4" y="0" width="10" height="5"/><rect x="0" y="5" width="18" height="7" rx="1"/><rect x="4" y="10" width="10" height="6"/></symbol>
    <symbol id="icon-mail" viewBox="0 0 18 16"><path d="M0 3h18v11H0z"/><path d="M0 3l9 6 9-6" fill="none" stroke="currentColor" stroke-width="1.4"/></symbol>
  </defs>
</svg>

<section class="card card--pink">
  <div class="brand-mark">Abbott<br>Women's<br>Health</div>
  <h1 class="doctor-name centered" style="top:190px">Corin Abbott-Whitmore MD</h1>
  <p class="credential centered" style="top:227px">Board Certified</p>
  <p class="specialty centered" style="top:252px">Women’s Health &amp; Wellness Specialist</p>
  <p class="appointment centered" style="top:282px">By Appointment</p>
  <ul class="services centered" style="top:324px">
    <li>Obstetrics</li><li>Gynecology</li><li>Family Planning</li><li>Menopause</li>
  </ul>
  <p class="address centered" style="top:474px">418 Alder Road, Brookfield NY 11090</p>
  <p class="contact" style="left:52px;top:508px;color:var(--pink)"><svg><use href="#icon-phone"/></svg><span style="color:var(--ink)">516.555.0148/0149</span></p>
  <p class="contact" style="left:52px;top:539px;color:var(--pink)"><svg><use href="#icon-fax"/></svg><span style="color:var(--ink)">516.555.0153</span></p>
  <p class="contact" style="left:52px;top:568px;color:var(--pink)"><svg><use href="#icon-mail"/></svg><span style="color:var(--ink)">c-abbott@mailhaven.net</span></p>
</section>

<section class="card card--lilac">
  <div class="brand-mark">Abbott<br>Women's<br>Health</div>
  <h1 class="doctor-name centered" style="top:157px">Corin Abbott-Whitmore MD</h1>
  <p class="credential centered" style="top:190px">Board Certified</p>
  <p class="specialty specialty--script centered" style="top:212px">Women’s Health<br>&amp; Wellness Specialist</p>
  <p class="appointment centered" style="top:276px">By Appointment</p>
  <ul class="services centered" style="top:316px">
    <li>Obstetrics</li><li>Gynecology</li><li>Family Planning</li><li>Weight Management</li><li>Menopause</li>
  </ul>
  <p class="address" style="left:52px;top:458px">207-14 Maple Parkway, Ridgeview<br>New York 11425</p>
  <p class="contact" style="left:52px;top:512px;color:var(--lilac)"><svg><use href="#icon-phone"/></svg><span style="color:var(--ink)">718.555.0125</span></p>
  <p class="contact" style="left:52px;top:543px;color:var(--lilac)"><svg><use href="#icon-fax"/></svg><span style="color:var(--ink)">718.555.0126</span></p>
  <p class="contact" style="left:52px;top:573px;color:var(--lilac)"><svg><use href="#icon-mail"/></svg><span style="color:var(--ink)">c-abbott@mailhaven.net</span></p>
</section>

</body>
</html>
```